Construction Company

Design a clutter free business card, it can be double-sided utilizing the logo for BDN Ltd simple with all relevant contact information.

Please also a letterhead design to function for the purposes of invoicing, all mail requirements, with header to be distinctive while the footer ties page together and incorporates all necessary information.

For now, please use generic / dummy text and when a winner is selected, I will disclose the contact information.

Hi Designers! Please read the updated brief which includes the design of a business card and letterhead. Thank you!

```html
<!DOCTYPE html>
<html lang="en">
<head>
<meta charset="utf-8">
<title>BDN Ltd – Business Card</title>
<link rel="stylesheet" href="https://fonts.googleapis.com/css2?family=Source+Sans+3:wght@300;700&display=swap">
<style>
  :root {
    --ink: #1b1d1d;
    --paper: #ffffff;
    --wedge: #d5d6d8;
    --ghost: #d2d2d2;
  }
  html, body {
    margin: 0;
    padding: 0;
    overflow: hidden;
    background: var(--paper);
  }
  .card {
    position: relative;
    width: 1200px;
    height: 705px;
    overflow: hidden;
    background: var(--paper);
    font-family: "Source Sans 3", "Myriad Pro", sans-serif;
    color: var(--ink);
  }
  .corner-wedge {
    position: absolute;
    inset: 0;
  }
  .accent-bar {
    position: absolute;
    left: 24px;
    top: 26px;
    width: 15px;
    height: 185px;
    background: var(--ink);
  }
  .ghost-name {
    position: absolute;
    left: 533px;
    top: 364px;
    transform: translate(-50%, -50%);
    margin: 0;
    font-weight: 700;
    font-size: 120px;
    line-height: 1;
    white-space: nowrap;
    color: var(--ghost);
  }
  .brand {
    position: absolute;
    left: 800px;
    top: 118px;
    display: flex;
    align-items: center;
    gap: 12px;
  }
  .brand-mark {
    width: 18px;
    height: 18px;
    background: var(--ink);
  }
  .brand-name {
    margin: 0;
    font-weight: 700;
    font-size: 64px;
    line-height: 1;
    color: var(--ink);
    white-space: nowrap;
  }
  .brand-tagline {
    position: absolute;
    left: 822px;
    top: 216px;
    margin: 0;
    font-weight: 300;
    font-size: 16px;
    letter-spacing: 0.2px;
  }
  .contact {
    position: absolute;
    left: 826px;
    top: 579px;
  }
  .contact-rule {
    width: 200px;
    height: 11px;
    background: var(--ink);
    margin-bottom: 4px;
  }
  .contact p {
    margin: 0;
    font-weight: 300;
    font-size: 16px;
    line-height: 22px;
  }
</style>
</head>
<body>
  <main class="card">
    <svg class="corner-wedge" width="1200" height="705" viewBox="0 0 1200 705" aria-hidden="true">
      <polygon points="1200,0 1200,705 803,705" fill="var(--wedge)"/>
    </svg>

    <div class="accent-bar"></div>

    <p class="ghost-name" aria-hidden="true">BDN Ltd</p>

    <div class="brand">
      <span class="brand-mark"></span>
      <h1 class="brand-name">BDN Ltd</h1>
    </div>
    <p class="brand-tagline">CONSTRUCTION COMPANY</p>

    <section class="contact">
      <div class="contact-rule"></div>
      <p>CONSTRUCTION COMPANY</p>
      <p>Address</p>
    </section>
  </main>
</body>
</html>
```